Produktbroschüre
Zielgruppe
Einzelhändler im Einrichtungs-, Geschenk- und Blumanfachhandel, Dekorateure, Innenarchitekten,
Aufgabenstellung
Ich bin Existenzgründer und brauche eine ansprechende Produktbroschüre für Inneneinrichtungsdeko und Accessoires.
Die Artikel wechseln öfter und ich möchte in der Lage sein Bilder und Texte einfach auszutauschen. Über die zeit, wird das Sortiment erwetert, die Broschüre sollte einfach mitwachsen können.
Momentan behelfe ich mir mit Scribus und Gimp für Windows, bin aber kein Experte.
Als Anhang meine momentane, selbst gebaute Broschüre.

```html
<!DOCTYPE html>
<html lang="de">
<head>
<meta charset="utf-8">
<title>Sorel Bunt – Produktbroschüre</title>
<link rel="stylesheet" href="https://fonts.googleapis.com/css2?family=Fira+Sans:wght@300;400;600&display=swap">
<style>
  :root {
    --orange: #f08a1c;
    --orange-line: #f3b27a;
    --paper: #ffffff;
    --ink-dark: #5b2c0c;
    --ink-grey: #555555;
    --page-bg: #eeeae4;
  }
  html, body {
    margin: 0;
    width: 1200px;
    height: 1200px;
    overflow: hidden;
    background: var(--page-bg);
    font-family: "Fira Sans", Arial, sans-serif;
  }
  .spread {
    position: absolute;
    left: 50px;
    top: 300px;
    width: 1100px;
    height: 600px;
    background: var(--paper);
    box-shadow: 0 2px 10px rgba(0,0,0,0.12);
  }
  .spread-shapes {
    position: absolute;
    inset: 0;
  }
  .brand-name {
    position: absolute;
    left: 62px;
    top: 208px;
    font-size: 15px;
    font-weight: 300;
    color: var(--orange);
  }
  .welcome {
    position: absolute;
    left: 130px;
    top: 240px;
    font-size: 18px;
    font-weight: 400;
    color: var(--ink-grey);
    white-space: nowrap;
  }
  .welcome-plus {
    position: absolute;
    left: 488px;
    top: 268px;
    font-size: 34px;
    font-weight: 300;
    color: var(--orange);
    line-height: 1;
  }
  .page-number {
    position: absolute;
    left: 70px;
    top: 532px;
    font-size: 13px;
    font-weight: 400;
    color: var(--paper);
  }
  .contents {
    position: absolute;
    left: 628px;
    top: 120px;
    margin: 0;
    padding: 0;
    list-style: none;
    font-size: 15px;
    line-height: 22px;
    color: var(--ink-dark);
    font-weight: 600;
  }
  .contents .pages {
    font-weight: 400;
    color: var(--paper);
  }
  .exclusive {
    position: absolute;
    left: 628px;
    top: 268px;
    font-size: 16px;
    font-weight: 600;
    color: var(--ink-dark);
  }
  .exclusive .shop {
    font-weight: 300;
  }
  .web-address {
    position: absolute;
    left: 640px;
    top: 548px;
    font-size: 14px;
    font-weight: 300;
    color: var(--orange-line);
  }
</style>
</head>
<body>
  <main class="spread">
    <svg class="spread-shapes" width="1100" height="600" viewBox="0 0 1100 600" aria-hidden="true">
      <path d="M40 25 H520 Q540 25 540 45 V440 Q540 458 522 458 H300 Q284 458 278 446 Q272 434 256 434 H40 Q22 434 22 416 V45 Q22 25 40 25 Z"
            fill="none" stroke="var(--orange-line)" stroke-width="1.2"/>
      <path d="M0 470 H220 Q238 470 244 482 Q250 494 268 494 H530 Q550 494 550 514 V560 Q550 575 535 575 H0 Z"
            fill="var(--orange)"/>
      <path d="M598 25 H1062 Q1082 25 1082 45 V470 Q1082 490 1062 490 H850 Q832 490 826 478 Q820 466 802 466 H598 Q578 466 578 446 V45 Q578 25 598 25 Z"
            fill="var(--orange)"/>
      <path d="M598 510 H760 Q776 510 782 522 Q788 534 804 534 H1062 Q1082 534 1082 554 V578 H578 V530 Q578 510 598 510 Z"
            fill="none" stroke="var(--orange-line)" stroke-width="1.2"/>
      <line x1="560" y1="0" x2="560" y2="600" stroke="#f1ece6" stroke-width="1"/>
    </svg>

    <div class="brand-name">sorel bunt</div>
    <div class="welcome">Herzlich Willkommen | Welcome | Bienvenue</div>
    <div class="welcome-plus">+</div>
    <div class="page-number">01</div>

    <ol class="contents">
      <li>01 Schalen <span class="pages">04 - 18</span></li>
      <li>02 Teelichthalter <span class="pages">19 - 28</span></li>
      <li>03 Vögel am Stiel <span class="pages">29 - 32</span></li>
      <li>04 Wippfiguren <span class="pages">33 - 40</span></li>
      <li>05 Bänke und Hocker <span class="pages">41 - 48</span></li>
      <li>06 Glanzrosen <span class="pages">59 - 60</span></li>
    </ol>
    <div class="exclusive">Exklusiv für Sie bei <span class="shop">sorel bunt</span></div>

    <div class="web-address">www.sorel-bunt.com</div>
  </main>
</body>
</html>
```